Packaging design for aloe lotion bottle for a Laser Clinic

We need a packaging design for a body lotion bottle. Our business is a laser clinic and we are looking at slowly rolling out a range of skincare products. This lotion bottle is the first item with more to follow so the winning designer will have other designs to work on in the future.

The design needs to be classy, elegant, strong and sophisticated. The bottle will be clear with a shiny silver sleeved lid. The lotion itself, which will be visible through the bottle, will be a very light green colour. Think Mirelle Vantrau and Doriva as that is the image I want to convey.

Ideally we were thinking of having a design with a single colour but if you come up with a fantastic multi colour design that we love then we're open to it.

Reason: I have extended the deadline as I feel I need more time to allow designers to submit their designs. I haven't found a design that I love just yet. The project has been made a guaranteed payment upon completion. Thank you.

Target Market(s)

upper class high income earners with a high disposable income. People that look after themselves

Industry/Entity Type

Beauty Salon

Colors
000000
cadf82

Requirements
Must have
• must include the details below:
• After Beam Soothing Balm
• This soothing and calming anti inflammatory cream is specifically formulated for use after post laser treatments.
• Fresh Cucumber, Melon and Aloe Vera Leaf Juice blend together in perfect harmony to quickly cool you skin and restore your skins natural moisture.
• Our luxurious calming cream targets redness and helps to reduce inflammation, bringing you supple and radiant skin like never before.
• Directions: Use a liberal amount twice daily on all your treatment areas. This nourishing cream can also be used daily to restore moisture and softness to areas of the face and body not being treated by laser or IPL.
• Ingredients: water (aqua), glycine soja (soybean) oil, cetyl alcohol, glycerin dimethicone, butyrospermum parkii (shea butter), theobroma cacao (cocoa) seed butter, aloe barbadensis (aloe vera) leaf juice, tocopheryl acetate, sodium ascorbyl phosphate, disodium EDTA, ceteareth-20, carbomer, BHT, benzyl benzoate, butylphenyl methylpropional, hexyl cinnamal, linalool, glyceryl caprylate, methylisothiazolinone. May contain: Red 4 (CI 14700, aka 504), Yellow 5 (CI 19140, Ki4), Yellow 6 (CI 15985, KI5), Blue 1 (CI 42090, Ao1), Red 33 (CI 17200, Aka 227), Ext. Violet 2 (CI 60730, Murasaki401), Green 3 (CI 42053, Midori3)
• Against Animal Testing
• Manufactured in Australia
• www.velvetbloomclinic.example.com.au
• 500ml
• Pure Glow Laser Hair Removal logo (see attached files)
Nice to have
• A sophisticated and elegant design
Should not have
• no photos. not too many different colours

```html
<!DOCTYPE html>
<html lang="en">
<head>
<meta charset="utf-8">
<title>Pure Glow Laser Hair Removal – After Beam Soothing Balm</title>
<link rel="stylesheet" href="https://fonts.googleapis.com/css2?family=Ubuntu:wght@300;400;500&display=swap">
<style>
  :root {
    --backdrop: #fdf7fb;
    --lotion-light: #e4fbb4;
    --lotion-mid: #d2f592;
    --lotion-deep: #c4ec7a;
    --shoulder: #eefbd9;
    --cap-dark: #8f8f8f;
    --cap-light: #e6e6e6;
    --label-black: #0c0c0c;
    --label-green: #b7e36a;
    --band-green: #8cc63f;
    --band-text: #f4ffe4;
  }
  html, body {
    margin: 0;
    padding: 0;
    width: 941px;
    height: 1200px;
    overflow: hidden;
    background: var(--backdrop);
  }
  .canvas {
    display: block;
    width: 941px;
    height: 1200px;
  }
  .brand-name, .brand-tagline, .product-kicker, .product-title, .claims, .blend-copy, .volume {
    font-family: "Ubuntu", sans-serif;
  }
  .brand-name { fill: var(--label-green); font-size: 62px; font-weight: 400; }
  .brand-tagline { fill: var(--label-green); font-size: 21px; font-weight: 400; }
  .product-kicker { fill: var(--label-green); font-size: 32px; font-weight: 300; }
  .product-title { fill: var(--label-green); font-size: 33px; font-weight: 400; }
  .claims { fill: var(--label-green); font-size: 18px; font-weight: 300; }
  .blend-copy { fill: var(--label-green); font-size: 18px; font-weight: 300; }
  .blend-copy .lead { font-weight: 500; }
  .volume { fill: var(--band-text); font-size: 17px; font-weight: 400; }
  .divider { stroke: var(--label-green); stroke-width: 1.2; }
  .divider-dot { fill: var(--label-green); }
</style>
</head>
<body>
<svg class="canvas" viewBox="0 0 941 1200" xmlns="http://www.w3.org/2000/svg">
  <defs>
    <linearGradient id="cap-sheen" x1="0" x2="1" y1="0" y2="0">
      <stop offset="0" stop-color="var(--cap-dark)"/>
      <stop offset="0.45" stop-color="var(--cap-light)"/>
      <stop offset="0.7" stop-color="#cfcfcf"/>
      <stop offset="1" stop-color="var(--cap-dark)"/>
    </linearGradient>
    <linearGradient id="lotion-fill" x1="0" x2="1" y1="0" y2="0">
      <stop offset="0" stop-color="var(--lotion-deep)"/>
      <stop offset="0.35" stop-color="var(--lotion-mid)"/>
      <stop offset="0.8" stop-color="var(--lotion-light)"/>
      <stop offset="1" stop-color="var(--lotion-mid)"/>
    </linearGradient>
  </defs>

  <g class="bottle">
    <rect class="bottle-cap" x="397" y="131" width="161" height="134" fill="url(#cap-sheen)"/>
    <path class="bottle-neck" d="M385 265 H570 L600 294 H291 Z" fill="var(--shoulder)"/>
    <path class="bottle-body" d="M291 294 H665 V1031 Q665 1071 625 1071 H331 Q291 1071 291 1031 Z" fill="url(#lotion-fill)"/>
    <rect class="bottle-shoulder" x="291" y="294" width="374" height="30" fill="var(--shoulder)" opacity="0.7"/>
  </g>

  <g class="label">
    <rect class="label-frame" x="311" y="385" width="328" height="557" fill="var(--label-black)"/>
    <rect class="label-inlay" x="317" y="391" width="316" height="545" fill="var(--label-green)"/>
    <rect class="label-panel" x="322" y="395" width="305" height="502" fill="var(--label-black)"/>
    <rect class="volume-band" x="322" y="897" width="305" height="26" fill="var(--band-green)"/>
    <rect class="label-foot" x="322" y="923" width="305" height="9" fill="var(--label-black)"/>

    <g class="brand">
      <text class="brand-name" transform="translate(398 798) rotate(-90)" textLength="369" lengthAdjust="spacingAndGlyphs">PURE GLOW</text>
      <text class="brand-tagline" transform="translate(425 798) rotate(-90)" textLength="366" lengthAdjust="spacing" letter-spacing="5">LASER HAIR REMOVAL</text>
    </g>

    <g class="product" text-anchor="end">
      <text class="product-kicker" x="617" y="457">after beam</text>
      <text class="product-title" x="617" y="495">SOOTHING</text>
      <text class="product-title" x="617" y="532">BALM</text>

      <line class="divider" x1="466" y1="559" x2="617" y2="559"/>
      <circle class="divider-dot" cx="541" cy="559" r="3"/>

      <text class="claims" x="617" y="602">soothing &amp; calming</text>
      <text class="claims" x="617" y="626">anti inflammatory</text>

      <line class="divider" x1="466" y1="657" x2="617" y2="657"/>
      <circle class="divider-dot" cx="541" cy="657" r="3"/>

      <text class="blend-copy" x="617" y="694"><tspan class="lead">Fresh Cucumber,</tspan></text>
      <text class="blend-copy" x="617" y="717"><tspan class="lead">Melon &amp; AloeVera</tspan></text>
      <text class="blend-copy" x="617" y="741">Leaf Juice blend</text>
      <text class="blend-copy" x="617" y="764">together in perfect</text>
      <text class="blend-copy" x="617" y="788">harmony to quickly</text>
      <text class="blend-copy" x="617" y="811">cool you skin and</text>
      <text class="blend-copy" x="617" y="834">restore your skins</text>
      <text class="blend-copy" x="617" y="857">natural moisture.</text>
    </g>

    <text class="volume" x="329" y="916">16.9 fl oz / 500 ml</text>
  </g>
</svg>
</body>
</html>
```